Event Website for the Audio & Visual Industry

Convene is an exhibition aimed at meeting the business needs of audio and visual professionals – the visitors are the ones that make purchase decisions when buying anything to do with AV installation, Lighting & Entertainment Technology, DJ Technologies and even Musical Instruments.

We need to rebuild our website to reflect the professional look but with a bit of creativity/flare that is associated with the industry.

Websites whose design is along the lines we're looking for:

• http:www.marlowtech.com.au
• http:www.quenra.com
• http://www.brightpanelfair.example/ (competitor expo, like the layout. Not fantastic though, but the best I’ve seen from the industry)
• http://www.velmora.com.au and http://www.tralvick.com.au/ (Like these brand websites, they are clean and corporate but the use of imagery allows it to have some personality)

Target Market(s)

Corporate AV End Users, Lighting Designers, Concert/Entertainment companies, Sound Engineers

Industry/Entity Type

Business

Requirements
Must have
• Refer to the current splash page – www.convene-expo.example
This is the look and feel we have developed for our brochure. We want to expand on this and create a professional corporate look and feel without alienating existing sound, light and vision sectors.

The website's focus is to register visitors to attend the show. Please include a floating 'Register Free' Call to action. Please also include floating social media buttons. For what I mean by 'floating' check out the Social media buttons on this website: http://feedlorn.example/2012/02/19/glass-tower-trailer/ (scroll down to see effect).

We'll like to include a Rotating Banner at the top.

Sponsor element at the bottom off the page.

Sign up form functionality

Menu to be: About the Show, What's On, Register, How to Exhibit, Blog, Contact us.

I would like to see designs for a content page as well as the homepage.

```html
<!DOCTYPE html>
<html lang="en">
<head>
<meta charset="utf-8">
<title>Convene – Audio Visual &amp; Entertainment Event</title>
<link href="https://fonts.googleapis.com/css2?family=Arimo:wght@400;700&family=Titillium+Web:wght@300;400&family=Noto+Sans:wght@400&family=Tinos&display=swap" rel="stylesheet">
<style>
:root{
  --page:#f6f6f6;
  --panel:#ffffff;
  --footer:#e6e6e6;
  --rule:#d8d8d8;
  --ink:#222;
  --headline:#3f7d98;
  --accent:#d6141c;
  --link:#6a1e1e;
  --blue-dark:#1d5f99;
  --gallery:#eefafc;
  --photo-a:#3a2c6b;
  --photo-b:#1b1830;
  --photo-c:#5b5f7a;
}
*{margin:0;padding:0;box-sizing:border-box}
html,body{width:1200px;height:1163px;overflow:hidden;background:#fff}
body{position:relative;font-family:"Arimo",Arial,sans-serif;color:var(--ink)}
.page{position:absolute;left:28px;top:0;width:1136px;height:1163px;background:var(--page)}
.abs{position:absolute;white-space:nowrap}

.brand{left:122px;top:92px;font-family:"Arimo",sans-serif;font-size:50px;color:#111;letter-spacing:-1px}

.nav{left:419px;top:121px;width:668px;height:63px;border:1px solid #ccc;border-radius:6px;background:#fafafa}
.nav a{position:absolute;top:22px;font-family:"Noto Sans",sans-serif;font-size:14px;color:#888;text-decoration:none}
.nav a.current{top:15px;left:15px;width:87px;height:31px;background:#e4e4e4;border:1px solid #bbb;border-radius:3px;color:#555;text-align:center;line-height:29px}

.rule{height:1px;background:var(--rule)}
.mosaic{left:113px;top:204px;width:443px;height:282px;display:grid;grid-template-columns:repeat(4,1fr);grid-template-rows:repeat(3,1fr);gap:2px}
.tile{background:linear-gradient(135deg,var(--photo-a),var(--photo-b))}
.tile:nth-child(3n){background:linear-gradient(135deg,var(--photo-c),var(--photo-b))}
.tile:nth-child(4n+2){background:linear-gradient(160deg,#5a3e8c,#201a3c)}

.intro{left:598px;top:203px;width:478px;height:284px;background:var(--panel);padding:8px 14px}
.intro h1{font-family:"Titillium Web",sans-serif;font-weight:300;font-size:29px;line-height:31px;color:var(--headline);letter-spacing:.3px}
.intro p{margin-top:21px;font-size:16px;line-height:23px;color:#555}

.date-band{left:190px;top:500px;width:820px;height:96px;background:radial-gradient(ellipse at 50% 30%,#fff 60%,#ececec 100%)}
.date{left:274px;top:519px;font-family:"Noto Sans",sans-serif;font-size:19px;color:var(--accent)}
.venue{left:273px;top:544px;font-family:"Noto Sans",sans-serif;font-size:14px;line-height:18px;color:#111}
.register{left:731px;top:523px;width:177px;height:48px;border-radius:5px;background:linear-gradient(#4f9ad6,var(--blue-dark));color:#fff;font-weight:700;font-size:19px;display:flex;align-items:center;justify-content:center;text-shadow:0 1px 1px #0b3a62}

.feature{left:95px;top:602px;width:998px;height:236px;background:var(--panel)}
.feature-title{left:115px;top:621px;width:405px;font-family:"Noto Sans",sans-serif;font-size:12px;line-height:18px;color:#222;padding-bottom:4px;border-bottom:1px solid #ccc}
.points{left:123px;top:676px;list-style:none}
.points li{display:flex;align-items:center;height:23.5px;font-family:"Noto Sans",sans-serif;font-size:12.5px;color:var(--link);letter-spacing:.2px}
.points li::before{content:"";width:14px;height:14px;border-radius:50%;border:1px solid #ddd;background:#f4f4f4;margin-right:15px}

.gallery{left:566px;top:608px;width:510px;height:220px;background:var(--gallery);border-radius:8px}
.gallery-title{left:602px;top:630px;font-family:"Noto Sans",sans-serif;font-size:18px;color:#111;padding-bottom:3px;border-bottom:2px dotted #6a8fc4;width:130px}
.thumbs{left:601px;top:679px;width:443px;height:92px;display:flex;gap:2px}
.thumbs .tile{flex:1}
.arrows{left:1013px;top:779px}

.footer{left:28px;top:838px;width:1136px;height:325px;background:var(--footer)}
.discover{left:101px;top:874px}
.discover h2{font-family:"Noto Sans",sans-serif;font-weight:400;font-size:14px;letter-spacing:.5px}
.discover p{margin-top:20px;font-family:"Noto Sans",sans-serif;font-size:11.5px;line-height:24px;color:#333}
.vline{width:1px;background:#bbb}
.news{left:527px;top:868px}
.news h2{font-family:"Noto Sans",sans-serif;font-weight:400;font-size:16px;padding-bottom:6px;border-bottom:1px dotted #bbb;width:296px}
.news p{margin-top:11px;font-size:11px;line-height:14px;color:#555}
.email{left:527px;top:946px;width:296px;height:33px;background:#fff;border:1px solid #ccc;font-size:10px;color:#aaa;padding:10px 12px;letter-spacing:1px}
.subscribe{left:527px;top:990px;width:163px;height:32px;border:1px solid #1b4c78;background:linear-gradient(#4e8fcc,#2f6aa6);color:#fff;font-family:"Tinos",serif;font-size:14px;padding:7px 12px}
.byline{left:876px;top:946px;display:flex;align-items:center;gap:8px;font-size:11px;color:#444}
.byline strong{font-size:20px;color:#555;letter-spacing:-.5px}
.legal{left:233px;top:1048px;width:744px;border-top:1px solid #c4c4c4;padding-top:8px;text-align:center;font-family:"Noto Sans",sans-serif;font-size:11px;line-height:18px;color:#666;letter-spacing:.4px}

.share{left:0;top:229px;width:60px;height:264px;background:#e4eef6;border-radius:0 6px 6px 0;padding:7px 0 0 4px;white-space:normal}
.count{width:44px;height:36px;border:1px solid #ccc;border-radius:3px;background:#fff;display:flex;align-items:center;justify-content:center;font-size:14px;color:#333;margin-bottom:5px}
.net{width:46px;height:18px;border:1px solid #bbb;border-radius:3px;background:#f4f4f4;font-size:10px;color:#2c5b85;display:flex;align-items:center;justify-content:center;margin-bottom:12px}
</style>
</head>
<body>
<div class="page"></div>

<div class="abs brand">Convene</div>

<nav class="abs nav">
  <a class="current">Home</a>
  <a style="left:127px">About the Show</a>
  <a style="left:274px">What's On</a>
  <a style="left:380px">How to Exhibit</a>
  <a style="left:517px">Blog</a>
  <a style="left:572px">Contact us</a>
</nav>

<div class="abs rule" style="left:113px;top:194px;width:981px"></div>

<div class="abs mosaic" role="img" aria-label="Grid of exhibition photos: mixing desks, lighting rigs, stands and crowds">
  <div class="tile"></div><div class="tile"></div><div class="tile"></div><div class="tile"></div>
  <div class="tile"></div><div class="tile"></div><div class="tile"></div><div class="tile"></div>
  <div class="tile"></div><div class="tile"></div><div class="tile"></div><div class="tile"></div>
</div>

<section class="abs intro">
  <h1>AUSTRALIA'S LARGEST<br>AUDIO VISUAL, ENTERTAINMENT &amp;<br>INFORMATION COMMUNICATIONS<br>TECHNOLOGY EVENT</h1>
  <p>With over 500 brands on display, Convene in association<br>with AvCircle Global, brings together the worlds of<br>ICT, integrating all areas including Visual, Education,<br>Entertainment, Audio &amp; Lighting Technology, Worship,<br>Digital Signage and Unified Communications.</p>
</section>

<div class="abs rule" style="left:113px;top:493px;width:981px"></div>
<div class="abs date-band"></div>
<div class="abs date">21st-23rd AUGUST 2012</div>
<div class="abs venue">harbourline convention &amp; Exhibition centre,Port Wenlow,<br>Australia</div>
<div class="abs register">Register Now</div>

<div class="abs feature"></div>
<div class="abs feature-title">BE PART OF AUSTRALIAS ONLY<br>EVENT FOR THE AUDIO VISUAL &amp; ENTERTAINMENT INDUSTRY</div>
<ul class="abs points">
  <li>NEW LOCATION</li><li>EVEV BIGGER SHOW</li><li>NEW SEMINAR</li><li>EVEV MORE SURPRISESS</li><li>DOWNLOAD THE FLOOR PLAN</li><li>CONTACT THE CONVENE TEAM</li>
</ul>

<div class="abs gallery"></div>
<div class="abs gallery-title">Photo Gallery</div>
<div class="abs thumbs" role="img" aria-label="Gallery thumbnails of show floor, audience and lit stands">
  <div class="tile"></div><div class="tile"></div><div class="tile"></div><div class="tile"></div>
</div>
<svg class="abs arrows" width="32" height="18" viewBox="0 0 32 18"><path d="M2 3l7 6-7 6M29 3l-7 6 7 6" fill="none" stroke="#555" stroke-width="3"/></svg>

<footer class="abs footer"></footer>
<div class="abs discover">
  <h2>DISCOVER THE LATEST ADVANCEMENTS IN...</h2>
  <p>Concert Production • AV Installation • Broadcast • Staging •<br>Lighting &amp; Entertainment Technology • Digital Media &amp; Infor-<br>mation Services • Education Technology • Post Production •<br>Multimedia • Audio Engineering • Recording • DJ Technologies<br>• Musical Instruments</p>
</div>
<div class="abs vline" style="left:490px;top:878px;height:138px"></div>
<div class="abs news">
  <h2>Newsletter</h2>
  <p>At vero eos et accusamus et iusto odio dignissimos ducimus<br>qui blanditiis praesentium</p>
</div>
<div class="abs email">your email address</div>
<div class="abs subscribe">Subscribe <span style="float:right">⟶</span></div>
<div class="abs vline" style="left:861px;top:878px;height:138px"></div>
<div class="abs byline">Brought to you by <strong>Harwell</strong></div>
<div class="abs legal">STRICTLY TRADE ONLY. Entry is restricted to members of the ICT, Audio Visual and Entertainment industries.<br>Persons not in these categories, including children will not be admitted at any time.<br>© 2011 Harwell Exhibitions, Austrlia. All rights reserved. Level 2, 118 Carrow Street, Port Wenlow, NSW<br>2999, Australia.<br>Telephone: +61 5550 1200. Facsimile: +61 5550 1281.</div>

<aside class="abs share">
  <div class="count">1,598</div><div class="net">Chirp</div>
  <div class="count" style="margin-top:-2px">18</div><div class="net">Plusly</div>
  <div class="count" style="color:#1d4f80;font-weight:700">433</div><div class="net">Linkwise</div>
  <div class="net">Pinlog</div>
</aside>
</body>
</html>
```